Electrical company business card design.

Hi, were an electrical company in Auckland New Zealand called Quenra Ltd. We focus mainly on high end residential and commercial so the card would be targeted towards that.
The card will be for myself, i am the director of the company.
Name: Derek Polworth
Position: Director/electrician
Phone: 021 387 9142
Email: derek@quenra-example.co.nz
Location: Auckland
As for colors the the blue color in the logo is preferred, i also don't mind a black background option.
Target Market(s)
High end residential and commercial
Industry/Entity Type
Electrician
Contact Information for Business Card
Name: Derek Polworth Position: Director/Electrician Phone: 021 387 9142, Email: derek@quenra-example.co.nz, Location: Auckland

```html
<!DOCTYPE html>
<html lang="en">
<head>
<meta charset="utf-8">
<title>Quenra Ltd – Business Card</title>
<link rel="stylesheet" href="https://fonts.googleapis.com/css2?family=Montserrat:wght@400;500&family=Ubuntu:wght@700&display=swap">
<style>
  :root {
    --backdrop: #9a9a9a;
    --card-white: #ffffff;
    --card-black: #191919;
    --brand-blue: #0f5aa8;
    --brand-blue-bright: #1b7fd1;
    --ink: #1d1d1d;
    --slate: #4c5157;
    --slate-dark: #50565c;
  }
  * { margin: 0; padding: 0; box-sizing: border-box; }
  html, body {
    width: 1093px; height: 1200px; overflow: hidden;
    background: var(--backdrop);
    font-family: "Montserrat", Arial, sans-serif;
  }
  .stage { position: relative; width: 1093px; height: 1200px; }

  .card {
    position: absolute; left: 265px; width: 595px;
    border-radius: 18px; overflow: hidden;
  }
  .card--front { top: 223px; height: 362px; background: var(--card-white); }
  .card--back { top: 616px; height: 365px; background: var(--card-black); }

  .brand { position: absolute; display: flex; align-items: center; }
  .brand__mark { background: var(--brand-blue-bright); flex: none; }
  .brand__name { font-weight: 500; letter-spacing: 0.02em; line-height: 1; }

  .card--front .brand { left: 58px; top: 184px; gap: 10px; }
  .card--front .brand__mark { width: 18px; height: 18px; }
  .card--front .brand__name { font-size: 36px; color: var(--slate); }

  .divider {
    position: absolute; left: 280px; top: 124px;
    width: 2px; height: 136px; background: var(--brand-blue);
  }

  .contact { position: absolute; left: 289px; top: 120px; color: var(--ink); }
  .contact__name {
    font-family: "Ubuntu", Arial, sans-serif; font-weight: 700;
    font-size: 24px; color: var(--brand-blue); line-height: 1.1;
  }
  .contact__role { font-size: 14px; margin-top: 3px; }
  .contact__city { font-size: 14.5px; margin-top: 11px; }
  .contact__list { list-style: none; margin-top: 6px; }
  .contact__item {
    display: flex; align-items: center; gap: 7px;
    font-size: 14px; height: 23px;
  }
  .contact__icon { width: 13px; height: 13px; fill: var(--brand-blue); flex: none; }

  .card--back .brand { left: 92px; top: 154px; gap: 18px; }
  .card--back .brand__mark { width: 30px; height: 30px; }
  .card--back .brand__name { font-size: 70px; color: var(--slate-dark); }
</style>
</head>
<body>
<main class="stage">

  <section class="card card--front" aria-label="Business card front">
    <div class="brand">
      <span class="brand__mark"></span>
      <span class="brand__name">QUENRA</span>
    </div>

    <div class="divider"></div>

    <div class="contact">
      <h1 class="contact__name">Derek Polworth</h1>
      <p class="contact__role">Director/electrician</p>
      <p class="contact__city">Auckland</p>
      <ul class="contact__list">
        <li class="contact__item">
          <svg class="contact__icon" viewBox="0 0 24 24" aria-hidden="true"><path d="M6.6 10.8a15.2 15.2 0 0 0 6.6 6.6l2.2-2.2a1 1 0 0 1 1-.25 11.4 11.4 0 0 0 3.6.57 1 1 0 0 1 1 1V20a1 1 0 0 1-1 1A17 17 0 0 1 3 4a1 1 0 0 1 1-1h3.5a1 1 0 0 1 1 1c0 1.25.2 2.45.57 3.57a1 1 0 0 1-.25 1z"/></svg>
          <span>021 387 9142</span>
        </li>
        <li class="contact__item">
          <svg class="contact__icon" viewBox="0 0 24 24" aria-hidden="true"><path d="M2 5h20v2l-10 6L2 7z M2 9l10 6 10-6v10H2z"/></svg>
          <span>derek@quenra-example.co.nz</span>
        </li>
        <li class="contact__item">
          <svg class="contact__icon" viewBox="0 0 24 24" aria-hidden="true"><circle cx="12" cy="12" r="10"/><path d="M7 7c2 0 3 1 3 3s-2 2-2 4-3 1-4 0M15 4c0 2 2 2 2 4s-2 3 0 5 3 1 4 1M12 22c0-3 2-3 3-5" stroke="#fff" stroke-width="1.6" fill="none"/></svg>
          <span>www.quenra-example.co.nz</span>
        </li>
      </ul>
    </div>
  </section>

  <section class="card card--back" aria-label="Business card back">
    <div class="brand">
      <span class="brand__mark"></span>
      <span class="brand__name">QUENRA</span>
    </div>
  </section>

</main>
</body>
</html>
```